cosmetic business needs inner and outer packaging

We, Velisto cosmetics, are a importer and oline retail of beauty products on an argan oil base. We will put 2 new products on the market.
A glass bottle 50ml of pure oil, and a 150g jar facemask.
Both need inner and outter packaging design.

Dimension of packaging:
Face mask jar:
- width : 20 cm - Height : 3 cm
Outter packaging:
- Width :  7,7 cm - height :  6,3 cm

Oil Bottle:
-Width : 10,4 cm - height : 4,3 cm
Outer packaging:
- Width :  3,8 cm - height :  12 cm

Pictures of the Jar & bottle are attached.

Our Brand:
Velisto design sources its products directly from the cooperatives in Morocco. The coorperatives are run by the local women. Therefore we support the local economy, independence of the woman and sustainable production.
We offer two classic beauty products. The pure argan oil, can be used for hair, skin or nails. It comes in a 50ml blue glass bottle.
A ghassoul face mask, comes in a jar of 150g.

For the design we envision a classicm, timeless design. Colours like lavendel, burgundy or indigo with specks of silver or gold. On the right side of the outter package we imagine an outline of what is inside. So a sillhouette of the jar/bottle.(see attached picture) But these are only ideas not limitations.
Attached some pictures of competitors.
If possible i would like to be able to amend the text as there cna be changes.

some competitors:
http://www.plumerin.co.uk/
http://www.kestrabow.co.uk/03_face_oil.html
https://orvinellu.com/

aldo obviously the logo has to be incoorperated in the packaging, so the bonus in the end will not demand any extra work

Target Market(s)

Taget marked:
Manily women, 26+ years, urban, interested in social and enviromental issues, earing money and able to spend on luxury products, interest in cosmetics,

Industry/Entity Type

Cosmetics

Logo Text

Velisto

Requirements
Must have
• amendable text on the back, as there are some legal requirements for cosmetic products.

```html
<!DOCTYPE html>
<html lang="en">
<head>
<meta charset="UTF-8">
<title>Velisto Cosmetics – Pure Argan Oil Label</title>
<link href="https://fonts.googleapis.com/css2?family=Playfair+Display:wght@500&family=PT+Serif:wght@400&display=swap" rel="stylesheet">
<style>
  :root {
    --canvas-bg: #ffffff;
    --label-top: #f4f3f5;
    --label-bottom: #e9e8eb;
    --ink: #2f2e33;
    --ink-soft: #4a4950;
    --lavender: #b6a9dc;
    --rule: #6d6c72;
  }
  * { margin: 0; padding: 0; box-sizing: border-box; }
  html, body {
    width: 1000px;
    height: 1200px;
    overflow: hidden;
    background: var(--canvas-bg);
  }
  .canvas {
    position: relative;
    width: 1000px;
    height: 1200px;
    background: var(--canvas-bg);
  }
  .label {
    position: absolute;
    left: 140px;
    top: 130px;
    width: 720px;
    height: 940px;
    background: linear-gradient(180deg, var(--label-top), var(--label-bottom));
    color: var(--ink);
  }
  .brand {
    position: absolute;
    top: 48px;
    left: 0;
    width: 100%;
    text-align: center;
    color: var(--ink);
    font-family: "PT Serif", Georgia, serif;
    font-weight: 400;
  }
  .brand-mark {
    display: block;
    width: 64px;
    height: 64px;
    margin: 0 auto 22px;
    border: 3px solid var(--ink);
    border-radius: 50%;
  }
  .brand-name {
    display: block;
    font-size: 46px;
    letter-spacing: 4px;
    line-height: 1;
  }
  .brand-sub {
    display: block;
    margin-top: 8px;
    font-size: 17px;
    letter-spacing: 9px;
    line-height: 1;
    padding-left: 9px;
  }
  .accent-bar {
    position: absolute;
    left: 84px;
    top: 318px;
    width: 12px;
    height: 236px;
    background: var(--lavender);
  }
  .product-title {
    position: absolute;
    left: 104px;
    top: 306px;
    font-family: "Playfair Display", Georgia, serif;
    font-weight: 500;
    font-size: 92px;
    line-height: 80px;
    letter-spacing: -1px;
    color: var(--ink);
  }
  .product-title span { display: block; }
  .title-rule {
    position: absolute;
    left: 104px;
    top: 604px;
    width: 520px;
    height: 3px;
    background: var(--rule);
  }
  .product-use {
    position: absolute;
    left: 106px;
    top: 622px;
    font-family: "PT Serif", Georgia, serif;
    font-size: 27px;
    letter-spacing: 0.5px;
    color: var(--ink-soft);
  }
  .product-volume {
    position: absolute;
    left: 0;
    top: 832px;
    width: 100%;
    text-align: center;
    font-family: "PT Serif", Georgia, serif;
    font-size: 26px;
    color: var(--ink-soft);
  }
</style>
</head>
<body>
  <main class="canvas">
    <section class="label">
      <div class="brand">
        <span class="brand-mark"></span>
        <span class="brand-name">VELISTO</span>
        <span class="brand-sub">COSMETICS</span>
      </div>
      <div class="accent-bar"></div>
      <h1 class="product-title">
        <span>PURE</span>
        <span>ARGAN</span>
        <span>OIL</span>
      </h1>
      <div class="title-rule"></div>
      <p class="product-use">FOR HAIR, SKIN OR NAILS</p>
      <p class="product-volume">50ml / 1.7 fl oz.</p>
    </section>
  </main>
</body>
</html>
```